Business cards for KORU Real Estate Holdings LLC

We need a cool, original business card design for a company based in the Washington DC metropolitan area. We are a new energetic and passionate Real Estate Investing Company that invests in all types of real estate; commercial, residential, industrial etc.

Our company color is Red since it reflects action, energy and speed; it is assertive confident, energizing, exciting, powerful, passionate and determined. So we would like business card communicate those qualities to the audience.

Our audiences are investors that want to invest with us, real estate sellers, buyers, and tenants who lease from us.

Our logo is attached

```html
<!DOCTYPE html>
<html lang="en">
<head>
<meta charset="utf-8">
<title>KORU Real Estate Holdings LLC — Business Cards</title>
<link rel="stylesheet" href="https://fonts.googleapis.com/css2?family=Open+Sans:wght@400;600;700&display=swap">
<style>
  :root {
    --page-bg: #e4e4e4;
    --red: #cf1f27;
    --red-deep: #8f1015;
    --charcoal: #3a3a3c;
    --charcoal-deep: #1f1f21;
    --white: #ffffff;
    --soft-grey: #c9c9c9;
    --ink: #333335;
  }
  * { box-sizing: border-box; margin: 0; padding: 0; }
  html, body {
    width: 1200px; height: 983px; overflow: hidden;
    background: var(--page-bg);
    font-family: "Open Sans", Arial, sans-serif;
  }
  .stage {
    width: 1200px; height: 983px;
    display: flex; flex-direction: column; align-items: center; justify-content: center;
    gap: 48px;
  }
  .card {
    position: relative; width: 760px; height: 434px; overflow: hidden;
    border-radius: 6px;
    box-shadow: 0 10px 28px rgba(0,0,0,0.28);
  }
  .card-art { position: absolute; inset: 0; width: 100%; height: 100%; display: block; }

  /* Back of card */
  .brand-block {
    position: absolute; left: 372px; top: 222px;
    display: flex; flex-direction: column; align-items: flex-start;
  }
  .brand-row { display: flex; align-items: center; gap: 14px; }
  .brand-dot {
    width: 46px; height: 46px; border-radius: 50%;
    background: var(--white);
  }
  .brand-name {
    font-weight: 600; font-size: 72px; line-height: 1; letter-spacing: 2px;
    color: var(--white);
  }
  .brand-tagline {
    margin-top: 4px; margin-left: 62px;
    font-size: 13px; font-weight: 600; letter-spacing: 1px; text-transform: uppercase;
    color: var(--white);
  }

  /* Front of card */
  .front-brand { position: absolute; left: 48px; top: 44px; }
  .front-brand .brand-dot { width: 40px; height: 40px; background: var(--red); }
  .front-brand .brand-name { font-size: 52px; color: var(--ink); }
  .front-brand .brand-tagline {
    margin-left: 54px; font-size: 12px; color: var(--ink);
  }
  .person { position: absolute; left: 44px; top: 318px; color: var(--white); }
  .person-name { font-weight: 700; font-size: 34px; line-height: 1.1; }
  .person-role { font-weight: 700; font-size: 20px; color: #e9a9ab; margin-top: 4px; }
  .contact-list {
    position: absolute; left: 440px; top: 314px; list-style: none;
    color: var(--white); font-size: 17px;
  }
  .contact-list li { display: flex; align-items: center; gap: 14px; height: 28px; }
  .contact-icon { width: 20px; height: 20px; flex: none; }
</style>
</head>
<body>
<main class="stage">

  <section class="card card-back" aria-label="Business card back">
    <svg class="card-art" viewBox="0 0 760 434" aria-hidden="true">
      <defs>
        <linearGradient id="backRed" x1="0" y1="0" x2="1" y2="1">
          <stop offset="0" stop-color="#e02a31"/>
          <stop offset="1" stop-color="#a3141a"/>
        </linearGradient>
        <linearGradient id="backDark" x1="0" y1="0" x2="1" y2="1">
          <stop offset="0" stop-color="#2a2a2c"/>
          <stop offset="1" stop-color="#4a4a4d"/>
        </linearGradient>
      </defs>
      <rect width="760" height="434" fill="url(#backRed)"/>
      <path d="M0 0 H470 C505 150 425 300 240 380 C190 402 150 420 110 434 H0 Z" fill="url(#backDark)"/>
      <path d="M470 0 C505 150 425 300 240 380 C190 402 150 420 110 434" fill="none" stroke="#ffffff" stroke-width="3"/>
    </svg>
    <div class="brand-block">
      <div class="brand-row">
        <span class="brand-dot"></span>
        <span class="brand-name">KORU</span>
      </div>
      <span class="brand-tagline">Real Estate Holdings LLC</span>
    </div>
  </section>

  <section class="card card-front" aria-label="Business card front">
    <svg class="card-art" viewBox="0 0 760 434" aria-hidden="true">
      <defs>
        <linearGradient id="frontRed" x1="0" y1="0" x2="0" y2="1">
          <stop offset="0" stop-color="#d9232b"/>
          <stop offset="1" stop-color="#8f1015"/>
        </linearGradient>
        <linearGradient id="swoosh" x1="0" y1="0" x2="1" y2="0">
          <stop offset="0" stop-color="#2a2a2c"/>
          <stop offset="1" stop-color="#5a5a5d"/>
        </linearGradient>
      </defs>
      <rect width="760" height="434" fill="#ffffff"/>
      <path d="M0 292 C220 236 500 176 760 70 V434 H0 Z" fill="url(#frontRed)"/>
      <path d="M0 292 C220 236 500 176 760 70" fill="none" stroke="#ffffff" stroke-width="4"/>
      <path d="M70 222 C50 246 80 266 150 262 C340 250 560 160 760 34 V58 C560 176 340 270 150 282 C60 288 20 258 70 222 Z" fill="url(#swoosh)"/>
    </svg>

    <div class="front-brand">
      <div class="brand-row">
        <span class="brand-dot"></span>
        <span class="brand-name">KORU</span>
      </div>
      <span class="brand-tagline">Real Estate Holdings LLC</span>
    </div>

    <div class="person">
      <p class="person-name">Alex.Morgan</p>
      <p class="person-role">Owner</p>
    </div>

    <ul class="contact-list">
      <li>
        <svg class="contact-icon" viewBox="0 0 20 20" aria-hidden="true"><rect x="2" y="4" width="16" height="12" fill="none" stroke="#fff" stroke-width="1.6"/><path d="M2 4 L10 11 L18 4" fill="none" stroke="#fff" stroke-width="1.6"/></svg>
        <span>www.korurealestate.com</span>
      </li>
      <li>
        <svg class="contact-icon" viewBox="0 0 20 20" aria-hidden="true"><circle cx="10" cy="10" r="8" fill="none" stroke="#fff" stroke-width="1.6"/><ellipse cx="10" cy="10" rx="3.5" ry="8" fill="none" stroke="#fff" stroke-width="1.2"/><path d="M2 10 H18" stroke="#fff" stroke-width="1.2"/></svg>
        <span>alex.morgan@korurealestate.com</span>
      </li>
      <li>
        <svg class="contact-icon" viewBox="0 0 20 20" aria-hidden="true"><path d="M3 7 C3 4 7 3 10 3 C13 3 17 4 17 7 L14 8 L13 6 C11 5.5 9 5.5 7 6 L6 8 Z" fill="#fff"/><rect x="5" y="10" width="10" height="7" rx="1" fill="#fff"/></svg>
        <span>0412 555 019</span>
      </li>
    </ul>
  </section>

</main>
</body>
</html>
```